TRVL-NINE Web Design

We are a Health, Safety, Environmental & Quality Recruitment Agency, our clients are major corporate Mining, Oil & Gas and Engineering companies. We have offices in Perth & Melbourne, Australia

The website should be very functional & easy to navigate

BUT REALLY LOOKING FOR WOW FACTOR!

Please Note: TRVL CORPORATE IS OUR OLD COMPANY THE NEW ONE IS "TRVL-NINE" 

Some idea's from our competitors:

http://www.guardlinepeak.com.au/
http://www.vantagehiring.com.au/
http://www.brightpick.com.au/
http://www.kovastaffing.co.uk/
http://www.jobmarrow.com/health-safety-environment-jobs

Would love to see some of our valued clients and there logos

still looking for wow factor

Industry/Entity Type

Mining

Requirements
Must have
• A place where candidates can upload there resumes & other contact details
• eg: http://www.guardlinepeak.com.au/candidates/register-your-resume/
• A place we can load jobs on to eg: http://www.guardlinepeak.com.au/vacancies/
• Contact details:
• Perth: 12 Kestrel Ave, West Perth, Western Australia 6005
• t: 08 7153 4406 | f: 08 7153 4470 |
• Melbourne: Level 1, 218 Arbour Lane, Melbourne, Victoria 3000
• t: 03 6214 5072| f: 03 6231 4095 |
• e: dennisk@trvlnine.com.au | w: http://www.trvlnine.com.au

```html
<!DOCTYPE html>
<html lang="en">
<head>
<meta charset="utf-8">
<title>TRVL-NINE | Health, Safety, Environment and Quality Recruitment</title>
<link rel="stylesheet" href="https://fonts.googleapis.com/css2?family=Questrial&family=Arimo:wght@400;700&family=Signika:wght@600&display=swap">
<style>
  :root {
    --ink: #2b2b2b;
    --muted: #333;
    --brand-blue: #29aae2;
    --sky-blue: #5fc0ea;
    --navy: #0d4d8c;
    --rule: #d6d6d6;
    --page: #ffffff;
    --footer: #000000;
    --sea-dark: #14232e;
    --sea-mid: #1d4a6a;
    --sea-light: #3a7fae;
    --badge: #cfcfcf;
  }
  * { box-sizing: border-box; margin: 0; padding: 0; }
  html, body { width: 1027px; height: 1200px; overflow: hidden; }
  body {
    position: relative;
    font-family: "Arimo", Arial, sans-serif;
    color: var(--ink);
    background: var(--sea-dark);
  }
  .backdrop {
    position: absolute; inset: 0;
    background:
      radial-gradient(ellipse 200px 420px at 128px 380px, rgba(80,160,220,.45), transparent 70%),
      radial-gradient(ellipse 200px 420px at 899px 380px, rgba(80,160,220,.45), transparent 70%),
      linear-gradient(180deg, var(--sea-mid) 0%, var(--sea-light) 38%, var(--sea-mid) 55%, var(--sea-dark) 80%);
  }
  .page {
    position: absolute; left: 128px; top: 0;
    width: 771px; height: 1200px;
    background: var(--page);
  }
  .brand {
    position: absolute; left: 0; right: 0; top: 26px;
    display: flex; justify-content: center; align-items: center; gap: 12px;
  }
  .brand-mark { width: 56px; height: 56px; background: #7f8c96; }
  .brand-name {
    font-family: "Questrial", sans-serif;
    font-size: 34px; color: #3a3a3a; letter-spacing: 1px;
  }
  .nav {
    position: absolute; left: 12px; top: 108px; width: 747px; height: 32px;
    border-top: 1px solid var(--rule);
    display: flex; justify-content: space-around; align-items: center;
    padding: 0 38px 0 20px;
    font-family: "Questrial", sans-serif; font-size: 14px; letter-spacing: 1.2px;
  }
  .nav a { color: #333; text-decoration: none; position: relative; }
  .nav a.is-current { color: var(--brand-blue); }
  .nav a.is-current::before {
    content: ""; position: absolute; left: 50%; top: -12px; margin-left: -5px;
    border: 5px solid transparent; border-top-color: var(--rule);
  }
  .slider {
    position: absolute; left: 12px; top: 142px; width: 747px; height: 321px;
  }
  .slide {
    position: absolute; inset: 0;
    background: linear-gradient(180deg, #7ea8d6 0%, #a9c4e2 55%, #4f6f8f 78%, #2f557e 100%);
  }
  .slider-arrow {
    position: absolute; top: 148px; width: 28px; height: 28px;
    background: #000; display: flex; align-items: center; justify-content: center;
  }
  .slider-arrow.prev { left: 7px; }
  .slider-arrow.next { right: 6px; }
  .slider-shadow { position: absolute; left: 0; top: 321px; width: 747px; height: 16px; }
  .tagline { position: absolute; left: 0; right: 0; top: 488px; text-align: center; }
  .tagline-lead { font-size: 30px; font-weight: 700; color: var(--sky-blue); line-height: 34px; }
  .tagline-sub { font-size: 22px; color: #333; line-height: 28px; }
  .rule { position: absolute; left: 0; right: 0; height: 1px; background: var(--rule); }
  .sectors {
    position: absolute; left: 13px; top: 593px; display: flex; gap: 6px;
  }
  .sector { width: 182px; text-align: center; }
  .sector-photo { height: 126px; box-shadow: 0 8px 10px -6px rgba(0,0,0,.45); }
  .sector-name {
    margin-top: 16px; font-family: "Signika", sans-serif; font-weight: 600;
    font-size: 12px; letter-spacing: .5px; color: var(--navy); text-transform: uppercase;
  }
  .intro { position: absolute; left: 0; right: 0; top: 799px; text-align: center; font-size: 14.5px; line-height: 19px; }
  .intro .lead { color: var(--brand-blue); }
  .intro .rest { color: var(--muted); }
  .roles-title {
    position: absolute; left: 0; right: 0; top: 886px; text-align: center;
    font-size: 15.5px; color: var(--brand-blue);
  }
  .roles { position: absolute; top: 925px; left: 0; right: 0; font-size: 10.5px; color: #222; }
  .roles ul { list-style: none; position: absolute; width: 200px; text-align: center; line-height: 18.8px; }
  .roles ul:nth-child(1) { left: 12px; }
  .roles ul:nth-child(2) { left: 170px; }
  .roles ul:nth-child(3) { left: 333px; }
  .roles ul:nth-child(4) { left: 523px; }
  .more {
    position: absolute; left: 0; right: 0; top: 1032px; text-align: center;
    font-size: 11px; color: #222;
  }
  .more .bullet { display: inline-block; margin: 0 8px 0 10px; border: 3px solid transparent; border-left: 4px solid #222; border-right: 0; vertical-align: middle; }
  .more a { color: var(--brand-blue); text-decoration: none; }
  .partners {
    position: absolute; left: 0; right: 0; top: 1104px;
    display: flex; justify-content: space-around; align-items: center; padding: 0 48px;
  }
  .partner-badge { height: 26px; background: var(--badge); border-radius: 3px; }
  .footer {
    position: absolute; left: 0; right: 0; top: 1161px; height: 39px;
    background: var(--footer); color: #fff; font-size: 10px;
    display: flex; align-items: center; padding: 0 16px 0 14px; gap: 14px;
  }
  .footer .item { display: flex; align-items: center; gap: 6px; }
  .footer .divider { color: #ccc; margin: 0 2px; }
  .footer .to-top { margin-left: auto; font-size: 11.5px; font-weight: 700; }
</style>
</head>
<body>
  <div class="backdrop" role="img" aria-label="Offshore oil platforms standing in a deep blue sea"></div>

  <main class="page">
    <header class="brand">
      <span class="brand-mark"></span>
      <span class="brand-name">trvlnine</span>
    </header>

    <nav class="nav">
      <a class="is-current" href="#">home</a>
      <a href="#">about us</a>
      <a href="#">positions we offer</a>
      <a href="#">candidates</a>
      <a href="#">employers</a>
      <a href="#">contact us</a>
    </nav>

    <section class="slider">
      <div class="slide" role="img" aria-label="Offshore drilling rig with a gas flare under a clear blue sky"></div>
      <span class="slider-arrow prev"><svg width="10" height="14" viewBox="0 0 10 14"><path d="M7 1 L2 7 L7 13" fill="none" stroke="#fff" stroke-width="1.6"/></svg></span>
      <span class="slider-arrow next"><svg width="10" height="14" viewBox="0 0 10 14"><path d="M3 1 L8 7 L3 13" fill="none" stroke="#fff" stroke-width="1.6"/></svg></span>
      <svg class="slider-shadow" viewBox="0 0 747 16" preserveAspectRatio="none">
        <defs><radialGradient id="dropShade" cx="50%" cy="0%" r="60%"><stop offset="0" stop-color="#000" stop-opacity=".28"/><stop offset="1" stop-color="#000" stop-opacity="0"/></radialGradient></defs>
        <path d="M0 0 H747 Q373 22 0 0Z" fill="url(#dropShade)"/>
      </svg>
    </section>

    <section class="tagline">
      <h1 class="tagline-lead">Australia’s number 1</h1>
      <p class="tagline-sub">Health, Safety, Environment and Quality recruitment group</p>
    </section>

    <div class="rule" style="top:558px"></div>

    <section class="sectors">
      <div class="sector">
        <div class="sector-photo" role="img" aria-label="Bulk carrier ship at a loading jetty" style="background:linear-gradient(180deg,#a9c9ea 0%,#c9dbee 50%,#44607c 75%,#3b6a96 100%)"></div>
        <p class="sector-name">Health &amp; Safety</p>
      </div>
      <div class="sector">
        <div class="sector-photo" role="img" aria-label="Close-up of gold ore" style="background:radial-gradient(circle at 50% 45%,#d8b45c 0%,#8d6f36 45%,#3c3020 100%)"></div>
        <p class="sector-name">Quality</p>
      </div>
      <div class="sector">
        <div class="sector-photo" role="img" aria-label="Red offshore rig in a harbour" style="background:linear-gradient(180deg,#9ab3cd 0%,#b9c8d6 35%,#c6442c 55%,#5a4c48 75%,#6e8396 100%)"></div>
        <p class="sector-name">Training</p>
      </div>
      <div class="sector">
        <div class="sector-photo" role="img" aria-label="Power station lit up at night beside water" style="background:linear-gradient(180deg,#12285a 0%,#274c86 50%,#1f3a45 70%,#c79a3a 85%,#1a2436 100%)"></div>
        <p class="sector-name">Environmental</p>
      </div>
    </section>

    <section class="intro">
      <p class="lead">TRVL NINE is a Perth-based independent, specialised recruitment company</p>
      <p class="rest">with a focus on Health, Safety, Environment and Quality positions within the resources sector.</p>
    </section>

    <div class="rule" style="top:863px"></div>

    <h2 class="roles-title" style="font-weight:400">Offering both contract and permanent placements, our areas of recruitment include:</h2>
    <section class="roles">
      <ul><li>OHS Officers</li><li>Safety Advisors</li><li>Occupational Hygienists</li></ul>
      <ul><li>Training Advisors</li><li>Training Superintendents</li><li>Training Managers</li></ul>
      <ul><li>Quality Control Specialists</li><li>QAQC Engineers</li><li>Project Quality Managers</li></ul>
      <ul><li>Environmental Officers</li><li>Environmental Scientists</li><li>Corporate Environmental Managers</li></ul>
    </section>

    <div class="rule" style="top:1002px"></div>

    <p class="more">For the complete list of positions we offer<span class="bullet"></span><a href="#">Click Here</a></p>

    <div class="rule" style="top:1076px"></div>

    <section class="partners" aria-label="Industry partners">
      <span class="partner-badge" style="width:72px"></span>
      <span class="partner-badge" style="width:92px;height:34px"></span>
      <span class="partner-badge" style="width:86px"></span>
      <span class="partner-badge" style="width:130px;height:22px"></span>
      <span class="partner-badge" style="width:128px;height:22px"></span>
    </section>

    <footer class="footer">
      <span class="item">
        <svg width="12" height="13" viewBox="0 0 12 13"><path d="M2.5 1 L4.5 1 L5.5 4 L4 5.2 Q5.3 8 7.8 9 L9 7.5 L11.5 8.5 L11.5 10.8 Q11 12 9.5 12 Q2 11 1 3 Q1 1.3 2.5 1Z" fill="#fff"/></svg>
        +61 (08) 7153 4488
      </span>
      <span class="item">
        <svg width="14" height="10" viewBox="0 0 14 10"><rect x="0.5" y="0.5" width="13" height="9" fill="#fff"/><path d="M0.5 0.5 L7 6 L13.5 0.5" fill="none" stroke="#000" stroke-width="1"/></svg>
        perth@trvlnine.com.au
      </span>
      <span class="divider">|</span>
      <span>© Copyright TRVL-NINE 2013. All Rights Reserved.</span>
      <span class="to-top">Back to top</span>
    </footer>
  </main>
</body>
</html>
```